Flip Book Reference Guide for Medical Offices

We are looking to take a PowerPoint presentation and turn it into a flip book for our front office staff to use as a quick reference when needed. We are hoping for someone to take a quick once over of the PowerPoint then take it to the next level and make it look beautiful and professional. Alignment, graphics and clarity of design can make or break these sorts of products… we have the message, now need to ensure it's received and that is where you will come into play.

Industry/Entity Type

Medical

```html
<!DOCTYPE html>
<html lang="en">
<head>
<meta charset="utf-8">
<title>Family Medicine – Front Desk Flip Book</title>
<link href="https://fonts.googleapis.com/css2?family=Bebas+Neue&family=Exo+2:wght@700&family=Open+Sans:wght@600;700&display=swap" rel="stylesheet">
<style>
  :root {
    --navy: #1d3466;
    --orange: #f7941d;
    --orange-light: #fdc78c;
    --paper: #ffffff;
    --backdrop: #2e2e2e;
  }
  * { margin: 0; padding: 0; box-sizing: border-box; }
  html, body { width: 1200px; height: 1200px; overflow: hidden; }
  body { background: var(--backdrop); position: relative; font-family: "Open Sans", sans-serif; }

  .card { position: absolute; background: var(--paper); overflow: hidden; }
  .card--front { left: 252px; top: 110px; width: 695px; height: 521px; }
  .card--back  { left: 254px; top: 661px; width: 693px; height: 495px; }

  .stripe { position: absolute; left: 0; width: 100%; }
  .stripe--light  { background: var(--orange-light); }
  .stripe--orange { background: var(--orange); }
  .stripe--navy   { background: var(--navy); }

  .front-header { position: absolute; left: 0; top: 12px; width: 100%; height: 242px; background: var(--navy); }
  .front-title {
    position: absolute; left: 46px; top: 102px;
    font-family: "Bebas Neue", sans-serif; font-size: 70px; line-height: 1;
    color: var(--paper); letter-spacing: 0.5px;
  }
  .front-subtitle {
    position: absolute; left: 46px; top: 170px;
    font-family: "Exo 2", sans-serif; font-weight: 700; font-size: 38px; line-height: 1;
    color: var(--paper);
  }

  .brand { position: absolute; display: flex; align-items: center; color: var(--orange);
    font-family: "Open Sans", sans-serif; font-weight: 700; white-space: nowrap; }
  .brand__dot { border-radius: 50%; background: var(--orange); flex: none; }
  .card--front .brand { left: 24px; top: 332px; font-size: 52px; gap: 16px; }
  .card--front .brand__dot { width: 30px; height: 30px; }
  .card--back .brand { left: 54px; top: 160px; font-size: 76px; gap: 22px; }
  .card--back .brand__dot { width: 42px; height: 42px; }

  .back-note {
    position: absolute; left: 0; top: 300px; width: 100%;
    text-align: center; color: var(--navy);
    font-weight: 700; font-size: 17px; line-height: 31px;
  }
</style>
</head>
<body>
  <section class="card card--front">
    <div class="stripe stripe--light" style="top:0;height:5px"></div>
    <div class="stripe stripe--orange" style="top:5px;height:7px"></div>
    <header class="front-header">
      <h1 class="front-title">Family Medicine</h1>
      <p class="front-subtitle">Front Desk Flip Book</p>
    </header>
    <div class="stripe stripe--orange" style="top:254px;height:6px"></div>
    <div class="stripe stripe--light" style="top:260px;height:6px"></div>
    <div class="brand"><span class="brand__dot"></span>Lumeria Care</div>
  </section>

  <section class="card card--back">
    <div class="stripe stripe--navy" style="top:0;height:23px"></div>
    <div class="stripe stripe--orange" style="top:23px;height:8px"></div>
    <div class="stripe stripe--light" style="top:31px;height:6px"></div>
    <div class="brand"><span class="brand__dot"></span>Lumeria Care</div>
    <p class="back-note">This flip book is meant to be a quick reference guide for the front desk.<br>If further clarification or detail is required please refer to the Standard<br>Operating Procedures (SOPs).</p>
  </section>
</body>
</html>
```